Coffeeshop menu for filter tip

We want to have a cannabis (coffeeshop) menu in the size 25mm wide x 60mm wide. Some examples attached.

it must have the following text:
Menu

WEED p/g
Velotrine €16
Cinderfox €14
Tide Rambler €14
Marigolden €16
Grand Pelican €14
Copper Comet €14

HASH p/g
Baltic Ember €12
Harbor Velvet€11
Plum Rova €14
Dusk Maple €10

Target Market(s)

tourist in Amsterdam

Requirements
Nice to have
• cannabis sign leaf
• No Cigarettes allowed symbol

```html
<!DOCTYPE html>
<html lang="en">
<head>
<meta charset="utf-8">
<title>Coffeeshop Menu – Filter Tip</title>
<link rel="stylesheet" href="https://fonts.googleapis.com/css2?family=Oswald:wght@600;700&family=Tinos:wght@400;700&display=swap">
<style>
  :root {
    --canvas: #ffffff;
    --wood-light: #c8ab95;
    --wood-mid: #9a6a55;
    --wood-dark: #6a2a22;
    --wood-deep: #4a1a19;
    --title-red: #e81d25;
    --white: #ffffff;
    --item-yellow: #fff200;
    --shadow: rgba(30, 8, 4, 0.75);
    --leaf-light: #7aa84a;
    --leaf-dark: #2f5a1e;
  }
  * { box-sizing: border-box; margin: 0; padding: 0; }
  html, body { width: 1200px; height: 1000px; overflow: hidden; background: var(--canvas); }

  .menu-card {
    position: absolute;
    left: 460px; top: 125px;
    width: 324px; height: 778px;
    background: linear-gradient(180deg,
      var(--wood-light) 0%,
      #bf9c85 25%,
      var(--wood-mid) 42%,
      var(--wood-dark) 62%,
      var(--wood-deep) 100%);
    overflow: hidden;
  }

  .city-title {
    position: absolute;
    top: 12px; left: 0; width: 100%;
    text-align: center;
    font-family: "Oswald", sans-serif;
    font-weight: 700;
    font-size: 42px;
    line-height: 48px;
    letter-spacing: 1px;
    color: var(--title-red);
    -webkit-text-stroke: 1.5px var(--white);
    paint-order: stroke fill;
    text-shadow: 2px 3px 4px var(--shadow);
  }

  .leaf-artwork {
    position: absolute;
    left: 85px; top: 60px;
    width: 170px; height: 175px;
    border-radius: 50% 50% 45% 45%;
    background: radial-gradient(ellipse at 50% 55%, var(--leaf-light) 0%, var(--leaf-dark) 55%, rgba(47, 90, 30, 0) 72%);
  }

  .menu-heading {
    position: absolute;
    top: 234px; left: 0; width: 100%;
    text-align: center;
    font-family: "Oswald", sans-serif;
    font-weight: 600;
    font-size: 33px;
    line-height: 40px;
    letter-spacing: 0.42em;
    text-indent: 0.42em;
    color: var(--white);
    text-shadow: 2px 3px 4px var(--shadow);
  }

  .price-box {
    position: absolute;
    left: 28px; width: 264px;
    border: 2px solid var(--white);
    box-shadow: 1px 2px 3px var(--shadow);
    font-family: "Tinos", serif;
  }
  .price-box legend {
    margin-inline: auto;
    padding: 0 8px;
    font-weight: 700;
    font-size: 26px;
    line-height: 30px;
    color: var(--white);
    text-shadow: 1px 2px 3px var(--shadow);
    word-spacing: 6px;
  }
  .price-box--weed { top: 292px; padding: 8px 0 5px; }
  .price-box--hash { top: 527px; padding: 8px 0 7px; }

  .price-list { list-style: none; }
  .price-list li {
    display: flex;
    height: 29.5px;
    align-items: center;
    font-size: 27px;
    color: var(--item-yellow);
    text-shadow: 2px 3px 3px var(--shadow);
  }
  .price-list .name { width: 179px; padding-left: 16px; white-space: nowrap; }
  .price-list .price { padding-left: 16px; }

  .no-smoking {
    position: absolute;
    top: 714px; left: 80px;
    display: flex; align-items: center; gap: 8px;
    font-family: "Tinos", serif;
    font-weight: 700;
    font-size: 20px;
    color: var(--white);
    text-shadow: 1px 2px 3px var(--shadow);
  }
</style>
</head>
<body>
  <main class="menu-card">
    <h1 class="city-title">AMSTERDAM</h1>
    <div class="leaf-artwork" role="img" aria-label="Green cannabis leaf illustration"></div>
    <h2 class="menu-heading">MENU</h2>

    <fieldset class="price-box price-box--weed">
      <legend>WEED p/g</legend>
      <ul class="price-list">
        <li><span class="name">Velotrine</span><span class="price">€16</span></li>
        <li><span class="name">Cinderfox</span><span class="price">€14</span></li>
        <li><span class="name">Tide Rambler</span><span class="price">€14</span></li>
        <li><span class="name">Marigolden</span><span class="price">€16</span></li>
        <li><span class="name">Grand Pelican</span><span class="price">€14</span></li>
        <li><span class="name">Copper Comet</span><span class="price">€14</span></li>
      </ul>
    </fieldset>

    <fieldset class="price-box price-box--hash">
      <legend>HASH p/g</legend>
      <ul class="price-list">
        <li><span class="name">Baltic Ember</span><span class="price">€12</span></li>
        <li><span class="name">Harbor Velvet</span><span class="price">€11</span></li>
        <li><span class="name">Plum Rova</span><span class="price">€14</span></li>
        <li><span class="name">Dusk Maple</span><span class="price">€10</span></li>
      </ul>
    </fieldset>

    <div class="no-smoking">
      <svg width="42" height="42" viewBox="0 0 42 42" aria-hidden="true">
        <circle cx="21" cy="21" r="19" fill="#ffffff" stroke="#d71920" stroke-width="3.5"/>
        <rect x="8" y="23" width="20" height="5" fill="#222"/>
        <rect x="28" y="23" width="5" height="5" fill="#222"/>
        <path d="M27 20c0-4 4-4 4-8s-3-4-3-6" fill="none" stroke="#222" stroke-width="1.8"/>
        <path d="M31 20c0-4 3-4 3-7" fill="none" stroke="#222" stroke-width="1.8"/>
        <line x1="8" y1="8" x2="34" y2="34" stroke="#d71920" stroke-width="3.5"/>
      </svg>
      <span>No Sigarets</span>
    </div>
  </main>
</body>
</html>
```